Postcard Design

We sell disposable examination gloves, Powdered Latex, Powderfree Latex, and Nitrile (Non-Latex) Powder free.

We sell to Doctors, Dentists, and Nursery Schools mostly.

Cases are packed 10 boxes of 100 gloves per case, and willing for this mailing promotion to do "Buy 8 boxes, get 2 free" plus free shipping. This is for new or renewed customers

corvelmail has done flyers for us before, so there is some of our art pieces there.

Thanks to all. I have enough great presentations to choose from. Those who haven't done it, I do want a return address on the address side of the postcard. The address is: 415 Marlowe Austin, Texas 78621 Thanks again.. great work

```html
<!DOCTYPE html>
<html lang="en">
<head>
<meta charset="utf-8">
<title>Palmera Medical Postcard</title>
<link rel="stylesheet" href="https://fonts.googleapis.com/css2?family=Archivo+Black&family=Open+Sans:wght@400;600;700&display=swap">
<style>
  :root {
    --page-bg: #e9e9e9;
    --card-white: #ffffff;
    --grey-light: #f2f2f2;
    --grey-mid: #b9b9b9;
    --grey-dark: #8f8f8f;
    --ink: #111111;
    --offer-red: #d7141b;
    --offer-wine: #8a1020;
    --headline-yellow: #ffe600;
    --headline-blue: #1f9fe0;
    --headline-pink: #e23c9a;
    --tag-green: #2e9d55;
    --tag-teal: #2f8fa6;
    --tag-brown: #5a3b2e;
    --rule: #9a9a9a;
    --label: #8a8a8a;
  }
  * { box-sizing: border-box; margin: 0; padding: 0; }
  html, body { width: 1200px; height: 1000px; overflow: hidden; }
  body { background: var(--page-bg); font-family: "Open Sans", sans-serif; position: relative; }

  .postcard {
    position: absolute; left: 255px; width: 690px; height: 460px;
    overflow: hidden; box-shadow: 0 6px 18px rgba(0,0,0,.18);
  }
  .postcard--front { top: 20px; background: radial-gradient(ellipse at 55% 40%, var(--grey-light) 0%, var(--grey-mid) 60%, var(--grey-dark) 100%); border: 10px solid var(--card-white); }
  .postcard--back { top: 515px; background: var(--card-white); }

  /* front */
  .headline {
    position: absolute; top: 16px; left: 190px; white-space: nowrap;
    font-family: "Archivo Black", sans-serif; font-size: 27px; letter-spacing: -0.3px;
    color: var(--headline-yellow);
    text-shadow: 3px 3px 0 var(--headline-blue), -2px -2px 0 var(--headline-pink);
  }
  .glove-types { position: absolute; top: 66px; left: 30px; list-style: none; }
  .glove-types li {
    display: block; width: max-content; color: #fff; font-size: 14px; font-weight: 600;
    padding: 1px 8px; margin-bottom: 3px; border: 1px solid #fff;
  }
  .glove-types .powdered { background: var(--tag-green); margin-left: 14px; }
  .glove-types .powderfree { background: var(--tag-teal); margin-left: 7px; }
  .glove-types .nonlatex { background: var(--tag-brown); }

  .box-photo { position: absolute; top: 150px; left: 26px; width: 200px; height: 95px; border-radius: 4px;
    background: linear-gradient(135deg, #f3ece4 0%, #d9cfc4 55%, #b9c9d6 100%); }
  .case-note { position: absolute; top: 252px; left: 60px; font-size: 12px; color: #333; }
  .glove-photo { position: absolute; top: 80px; left: 330px; width: 240px; height: 330px; border-radius: 110px 110px 20px 20px;
    background: linear-gradient(160deg, #fbf8f2 0%, #e8e2d8 60%, #d8d0c2 100%); }

  .offer { position: absolute; top: 282px; left: 40px; font-family: "Archivo Black", sans-serif; color: var(--ink); line-height: 0.9;
    text-shadow: 2px 0 0 #fff, -2px 0 0 #fff, 0 2px 0 #fff, 0 -2px 0 #fff, 3px 4px 4px rgba(0,0,0,.35); }
  .offer .row { display: flex; align-items: baseline; }
  .offer .buy { font-size: 52px; padding-left: 80px; }
  .offer .unit { font-size: 24px; margin-left: 6px; font-family: "Open Sans", sans-serif; font-weight: 600; }
  .offer .get { font-size: 32px; padding-left: 40px; }
  .offer .two { font-size: 96px; color: var(--offer-red); margin: -20px 4px 0; }
  .offer .free { font-size: 58px; }
  .offer .mark { font-size: 30px; margin-left: 8px; align-self: flex-start; }

  .footnote { position: absolute; left: 6px; top: 430px; transform: rotate(-90deg); transform-origin: left top;
    font-size: 8px; color: #333; white-space: nowrap; }

  .corner-badge { position: absolute; right: -10px; bottom: -10px; width: 170px; height: 120px; }
  .brand { position: absolute; font-family: "Open Sans", sans-serif; font-weight: 700; color: var(--ink); white-space: nowrap; }
  .postcard--front .brand { right: 16px; bottom: 24px; font-size: 16px; }

  /* back */
  .back-offer { position: absolute; top: 22px; left: 60px; font-family: "Archivo Black", sans-serif; color: var(--ink); line-height: 0.95; }
  .back-offer .line1 { font-size: 36px; }
  .back-offer .line2 { font-size: 36px; padding-left: 130px; display: flex; align-items: baseline; gap: 6px; margin-top: -6px; }
  .back-offer .two { font-size: 64px; color: var(--offer-wine); }
  .back-box-photo { position: absolute; top: 66px; left: 50px; width: 120px; height: 48px; border-radius: 3px;
    background: linear-gradient(135deg, #f3ece4 0%, #d9cfc4 55%, #b9c9d6 100%); }
  .contact-form { position: absolute; top: 140px; left: 40px; width: 280px; }
  .contact-form .field { display: flex; align-items: flex-end; height: 26px; font-size: 11px; color: var(--label); }
  .contact-form .field span { width: 60px; }
  .contact-form .field i { flex: 1; border-bottom: 1px solid var(--rule); margin-bottom: 3px; }
  .postcard--back .brand { left: 40px; bottom: 40px; font-size: 18px; }
  .divider { position: absolute; left: 350px; top: 150px; height: 270px; border-left: 1px solid var(--rule); }
  .stamp-box { position: absolute; top: 40px; right: 40px; width: 90px; height: 110px; border: 1.5px solid #555; }
  .address-lines { position: absolute; top: 230px; left: 390px; width: 260px; }
  .address-lines i { display: block; height: 32px; border-bottom: 1px solid var(--rule); }
</style>
</head>
<body>

<section class="postcard postcard--front" aria-label="Postcard front">
  <h1 class="headline">Disposable Examination Gloves</h1>
  <ul class="glove-types">
    <li class="powdered">Powdered Latex</li>
    <li class="powderfree">Powderfree Latex</li>
    <li class="nonlatex">(Non Latex) Powder free</li>
  </ul>
  <div class="box-photo" role="img" aria-label="Photo of three glove boxes"></div>
  <p class="case-note">100 gloves per case</p>
  <div class="glove-photo" role="img" aria-label="Photo of a hand wearing a white latex examination glove"></div>
  <div class="offer">
    <div class="row buy">BUY 8<span class="unit">boxes</span></div>
    <div class="row get">get<span class="two">2</span><span class="free">FREE</span><span class="mark">*</span></div>
  </div>
  <p class="footnote">* Plus free shipping. This is for new or renewed customers.</p>
  <svg class="corner-badge" viewBox="0 0 170 120" aria-hidden="true">
    <circle cx="170" cy="120" r="140" fill="#ffffff"/>
  </svg>
  <div class="brand">Palmera Medical</div>
</section>

<section class="postcard postcard--back" aria-label="Postcard address side">
  <div class="back-offer">
    <div class="line1">BUY 8 BOXES</div>
    <div class="line2">get<span class="two">2</span>FREE</div>
  </div>
  <div class="back-box-photo" role="img" aria-label="Photo of glove boxes"></div>
  <div class="contact-form">
    <div class="field"><span>Name</span><i></i></div>
    <div class="field"><span>Email</span><i></i></div>
    <div class="field"><span>Referral</span><i></i></div>
    <div class="field"><span>Phone</span><i></i></div>
  </div>
  <div class="brand">Palmera Medical</div>
  <div class="divider"></div>
  <div class="stamp-box"></div>
  <div class="address-lines"><i></i><i></i><i></i><i></i><i></i></div>
</section>

</body>
</html>
```